Balvoramix Sharepoint Website

We are using Office365 so the website needs to be developed using SharePoint (Public Site). We are a technology company that provides IT sales and service so the website needs to address both. The site needs to be eye catching yet professional.

The sales portion of the sites must allow for easy updates, i.e. adding new products, update prices of current products, and ability to highlight specials events or special products.

A shopping cart is required. However, "check out" should allow the cart to be send to our sales department and someone will contact the user to finalize the sale.

Examples of websites we like are:

- http://www.plumvestaro.example/
- http://www.qnp.example/

It Company

```html
<!DOCTYPE html>
<html lang="en">
<head>
<meta charset="utf-8">
<title>Balvoramix – IT Sales &amp; Service</title>
<link href="https://fonts.googleapis.com/css2?family=Open+Sans:wght@400;600;700&family=Oswald:wght@300;400;600&family=Playfair+Display:wght@700&display=swap" rel="stylesheet">
<style>
:root{
  --red:#e2262b;
  --black:#111;
  --dark:#1c1c1c;
  --ink:#222;
  --grey:#6b6b6b;
  --light:#ececec;
  --band:#7a7a7a;
  --white:#fff;
  --line:#d8d8d8;
}
*{margin:0;padding:0;box-sizing:border-box}
html,body{width:1200px;height:2658px;overflow:hidden;background:var(--white)}
body{font-family:"Open Sans",Arial,sans-serif;color:var(--ink);position:relative}
.abs{position:absolute}

/* top bar */
.topbar{left:0;top:0;width:1200px;height:22px;background:var(--black);color:#ddd;font-size:10px;line-height:22px;padding:0 60px;display:flex;justify-content:space-between}
.topbar .account{display:flex;gap:22px}
.topbar .account span::before{content:"";display:inline-block;width:6px;height:6px;background:var(--red);border-radius:50%;margin-right:5px;vertical-align:middle}

/* header */
.logo{font-family:"Playfair Display",Georgia,serif;font-weight:700;letter-spacing:1px}
.brand{left:0;width:1200px;top:58px;text-align:center;font-size:44px;color:var(--ink)}
.search{left:856px;top:80px;width:226px;height:40px;display:flex}
.search .field{flex:1;border:1px solid var(--line);font-size:10px;color:#999;line-height:38px;padding-left:12px}
.search .btn{width:42px;background:var(--black);display:flex;align-items:center;justify-content:center}

.nav{left:84px;top:168px;width:1040px;height:32px;border-bottom:1px solid var(--line);display:flex;justify-content:center;gap:46px;font-size:11px;font-weight:600;text-transform:uppercase}
.nav a{color:var(--ink);text-decoration:none;line-height:30px;padding:0 4px}
.nav a.active{border-bottom:3px solid var(--red)}

/* hero */
.hero{left:0;top:216px;width:1200px;height:430px;background:linear-gradient(90deg,#050505 0%,#1a1a1a 45%,#2e2e2e 70%,#0c0c0c 100%)}
.hero-photo{left:470px;top:20px;width:660px;height:380px;background:radial-gradient(ellipse at 55% 50%,#cfcfcf 0%,#6d6d6d 35%,#262626 65%,transparent 80%)}
.hero h1{left:114px;top:60px;font-family:"Oswald",Arial,sans-serif;font-weight:300;font-size:76px;line-height:78px;color:var(--white);letter-spacing:1px}
.hero p{left:116px;top:230px;color:#ddd;font-size:15px}
.btn-red{background:var(--red);color:var(--white);font-family:"Oswald",Arial,sans-serif;text-transform:uppercase}
.hero .btn-red{left:114px;top:280px;width:150px;height:46px;font-size:22px;line-height:46px;text-align:center}

/* promos */
.promo{top:684px;width:334px;height:208px;background:var(--dark)}
.promo .img{left:170px;top:16px;width:150px;height:130px;background:radial-gradient(circle,#8a2a2a 0%,#3a3a3a 55%,#1c1c1c 80%)}
.promo h3{left:18px;top:108px;font-family:"Oswald",Arial,sans-serif;font-weight:400;font-size:22px;line-height:24px;color:var(--white)}
.promo p{left:18px;top:162px;font-size:10px;color:#bbb}
.promo .btn-red{right:14px;top:170px;width:90px;height:26px;font-size:14px;line-height:26px;text-align:center}

/* featured */
.featured-title{left:103px;top:940px;font-family:"Oswald",Arial,sans-serif;font-size:26px;font-weight:400;color:var(--ink)}
.featured-title em{font-style:normal;color:var(--red)}
.tile{width:170px}
.tile .img{width:170px;height:168px;border:1px solid #e2e2e2;box-shadow:0 2px 4px rgba(0,0,0,.08);display:flex;align-items:center;justify-content:center}
.img.mouse span{width:130px;height:96px;border-radius:48px;background:linear-gradient(135deg,#3db34a 0%,#d8d8d8 50%,#e34b50 100%)}
.img.tablet span{width:96px;height:124px;border-radius:8px;background:radial-gradient(circle,#c3262b 0%,#2a2a2a 45%,#0d0d0d 100%)}
.tile h4{font-size:12px;font-weight:400;margin-top:12px;padding-left:20px}
.tile .price{font-size:12px;color:var(--red);padding-left:20px}
.side-ad{left:904px;width:220px;height:218px;background:linear-gradient(160deg,#3f8ed6 0%,#1d4f8c 60%,#0f2a4d 100%)}
.side-ad.red{background:linear-gradient(160deg,#e2262b 0%,#8f1418 60%,#2a0a0b 100%)}

/* carousel */
.carousel{left:0;top:1860px;width:1200px;height:248px;background:var(--light)}
.carousel .arrow{top:96px}
.car-item{top:40px;width:170px;text-align:center;font-size:13px}
.car-item .img{width:170px;height:130px;margin-bottom:14px;background:radial-gradient(ellipse,#b9b9b9 0%,#e2e2e2 55%,var(--light) 75%)}

/* offers band */
.offers{left:0;top:2138px;width:1200px;height:216px;background:var(--band)}
.offer{top:72px;width:354px;height:66px;background:var(--white);display:flex;align-items:center;gap:14px;padding-left:18px}
.offer .icon{width:48px;height:40px;display:flex;align-items:center;justify-content:center}
.offer strong{display:block;font-family:"Oswald",Arial,sans-serif;font-weight:600;font-size:22px;line-height:24px;color:var(--ink)}
.offer small{font-size:10px;color:var(--grey)}

/* info strip */
.info{left:0;top:2354px;width:1200px;height:76px;display:flex;align-items:center;justify-content:center;gap:36px;font-size:11px}
.info b{color:var(--red)}
.info .tag{background:var(--red);color:var(--white);padding:4px 10px}

/* footer */
.footer{left:0;top:2430px;width:1200px;height:190px;background:var(--black);border-top:10px solid var(--red);color:#ccc}
.footer .logo{left:60px;top:40px;font-size:40px;color:var(--white)}
.footer .tagline{left:60px;top:96px;font-family:"Playfair Display",Georgia,serif;font-size:18px;color:var(--white);letter-spacing:1px}
.fcol{top:30px;font-size:10px;line-height:15px;list-style:none}
.follow{left:0;width:1200px;top:124px;text-align:center;font-size:11px}
.socials{display:flex;justify-content:center;gap:8px;margin-top:6px}
.socials span{width:18px;height:18px;border-radius:3px;background:#4a4a4a}

.partners{left:0;top:2620px;width:1200px;height:38px;display:flex;align-items:center;gap:22px;padding-left:60px;font-size:11px;color:var(--grey)}
.partners .badge{width:56px;height:20px;border-radius:3px;background:#d6d6d6}
</style>
</head>
<body>

<div class="abs topbar">
  <div>Register | Login</div>
  <div class="account"><span>Home</span><span>My Account</span><span>My Cart</span><span>Wishlist</span></div>
</div>

<div class="abs brand logo">Balvoramix</div>
<div class="abs search">
  <div class="field">SEARCH THE PRODUCT</div>
  <div class="btn"><svg width="18" height="18" viewBox="0 0 18 18"><circle cx="7.5" cy="7.5" r="5.5" fill="none" stroke="#fff" stroke-width="2"/><line x1="11.5" y1="11.5" x2="16" y2="16" stroke="#fff" stroke-width="2.4"/></svg></div>
</div>

<nav class="abs nav">
  <a class="active" href="#">Hardware</a><a href="#">Software</a><a href="#">Recent Products</a><a href="#">Brands</a><a href="#">Services</a><a href="#">All Products</a><a href="#">Contact Us</a>
</nav>

<section class="abs hero">
  <div class="abs hero-photo" role="img" aria-label="Open silver laptops on a dark background"></div>
  <h1 class="abs">NEW<br>ARRIVALS</h1>
  <p class="abs">Lorem ipsum dolor sit amet, consectetur adipisicing elit</p>
  <div class="abs btn-red">Buy Now</div>
</section>

<div class="abs promo" style="left:84px">
  <div class="abs img" role="img" aria-label="Desktop monitors"></div>
  <h3 class="abs">LOREM LIPSUM<br>ESDETE</h3><p class="abs">Lorem ipsum dolor</p><div class="abs btn-red">Buy Now</div>
</div>
<div class="abs promo" style="left:437px">
  <div class="abs img" role="img" aria-label="Red over-ear headphones"></div>
  <h3 class="abs">LOREM LIPSUM<br>ESDETE</h3><p class="abs">Lorem ipsum dolor</p><div class="abs btn-red">Buy Now</div>
</div>
<div class="abs promo" style="left:790px">
  <div class="abs img" role="img" aria-label="Game console controller"></div>
  <h3 class="abs">LOREM LIPSUM<br>ESDETE</h3><p class="abs">Lorem ipsum dolor</p><div class="abs btn-red">Buy Now</div>
</div>

<h2 class="abs featured-title">FEATURED <em>PRODUCTS</em></h2>

<!-- row 1 -->
<div class="abs tile" style="left:103px;top:1006px"><div class="img mouse" role="img" aria-label="Wireless mice in green, white and red"><span></span></div><h4>Wireless Mouse</h4><div class="price">$7.99</div></div>
<div class="abs tile" style="left:296px;top:1006px"><div class="img tablet" role="img" aria-label="Tablet showing headphones"><span></span></div><h4>Tablet Vantor</h4><div class="price">$21.99</div></div>
<div class="abs tile" style="left:490px;top:1006px"><div class="img mouse" role="img" aria-label="Wireless mice in green, white and red"><span></span></div><h4>Wireless Mouse</h4><div class="price">$7.99</div></div>
<div class="abs tile" style="left:684px;top:1006px"><div class="img tablet" role="img" aria-label="Tablet showing headphones"><span></span></div><h4>Tablet Vantor</h4><div class="price">$21.99</div></div>
<!-- row 2 -->
<div class="abs tile" style="left:103px;top:1272px"><div class="img tablet" role="img" aria-label="Tablet showing headphones"><span></span></div><h4>Tablet Vantor</h4><div class="price">$21.99</div></div>
<div class="abs tile" style="left:296px;top:1272px"><div class="img mouse" role="img" aria-label="Wireless mice in green, white and red"><span></span></div><h4>Wireless Mouse</h4><div class="price">$7.99</div></div>
<div class="abs tile" style="left:490px;top:1272px"><div class="img tablet" role="img" aria-label="Tablet showing headphones"><span></span></div><h4>Tablet Vantor</h4><div class="price">$21.99</div></div>
<div class="abs tile" style="left:684px;top:1272px"><div class="img mouse" role="img" aria-label="Wireless mice in green, white and red"><span></span></div><h4>Wireless Mouse</h4><div class="price">$7.99</div></div>
<!-- row 3 -->
<div class="abs tile" style="left:103px;top:1538px"><div class="img mouse" role="img" aria-label="Wireless mice in green, white and red"><span></span></div><h4>Wireless Mouse</h4><div class="price">$7.99</div></div>
<div class="abs tile" style="left:296px;top:1538px"><div class="img tablet" role="img" aria-label="Tablet showing headphones"><span></span></div><h4>Tablet Vantor</h4><div class="price">$21.99</div></div>
<div class="abs tile" style="left:490px;top:1538px"><div class="img mouse" role="img" aria-label="Wireless mice in green, white and red"><span></span></div><h4>Wireless Mouse</h4><div class="price">$7.99</div></div>
<div class="abs tile" style="left:684px;top:1538px"><div class="img tablet" role="img" aria-label="Tablet showing headphones"><span></span></div><h4>Tablet Vantor</h4><div class="price">$21.99</div></div>

<div class="abs side-ad" style="top:1006px" role="img" aria-label="Video games promotion banner with console and controller"></div>
<div class="abs side-ad red" style="top:1260px" role="img" aria-label="Video and audio promotion banner with headphones"></div>
<div class="abs side-ad" style="top:1518px" role="img" aria-label="Video games promotion banner with console and controller"></div>

<section class="abs carousel">
  <svg class="abs arrow" style="left:140px" width="20" height="34" viewBox="0 0 20 34"><polyline points="16,3 4,17 16,31" fill="none" stroke="#333" stroke-width="3"/></svg>
  <svg class="abs arrow" style="left:1040px" width="20" height="34" viewBox="0 0 20 34"><polyline points="4,3 16,17 4,31" fill="none" stroke="#333" stroke-width="3"/></svg>
  <div class="abs car-item" style="left:200px"><div class="img" role="img" aria-label="White computer mouse"></div>Lorem Ipsum</div>
  <div class="abs car-item" style="left:400px"><div class="img" role="img" aria-label="Plasma ball lamp"></div>Lorem Ipsum</div>
  <div class="abs car-item" style="left:600px"><div class="img" role="img" aria-label="Black wireless mouse"></div>Lorem Ipsum</div>
  <div class="abs car-item" style="left:800px"><div class="img" role="img" aria-label="Black remote presenter"></div>Lorem Ipsum</div>
</section>

<section class="abs offers">
  <div class="abs offer" style="left:236px">
    <div class="icon"><svg width="46" height="32" viewBox="0 0 46 32"><rect x="1" y="5" width="28" height="18" fill="#222"/><path d="M29 10h9l6 7v6H29z" fill="#222"/><circle cx="9" cy="26" r="4" fill="#e2262b"/><circle cx="36" cy="26" r="4" fill="#e2262b"/></svg></div>
    <div><strong>FREE SHIPPING !</strong><small>Free shipping on orders over $100</small></div>
  </div>
  <div class="abs offer" style="left:638px">
    <div class="icon"><svg width="44" height="36" viewBox="0 0 44 36"><path d="M2 6h30l10 12-10 12H2z" fill="#e2262b"/><circle cx="30" cy="18" r="3" fill="#fff"/></svg></div>
    <div><strong>20% DISCOUNT</strong><small>Apply for long time customers</small></div>
  </div>
</section>

<div class="abs info">
  <span><b>FREE SHIPPING</b> on all orders over $50.00</span>
  <span><b>SUPPORT ANYTIME</b> 0123 456 789</span>
  <span class="tag">Offer of the day</span>
  <span>Additional <b>10%</b> off for orders over $100.00</span>
</div>

<footer class="abs footer">
  <div class="abs logo">Balvoramix</div>
  <div class="abs tagline">LOREM IPSUM ESDETE</div>
  <ul class="abs fcol" style="left:400px"><li>Get To Know Us</li><li>Our Store</li><li>Corporate</li><li>Community Giving</li><li>Product Feedback</li><li>Our Blog</li></ul>
  <ul class="abs fcol" style="left:590px"><li>Need Help?</li><li>Contact Us</li><li>Customer Services</li><li>My Order Account</li><li>FAQ</li></ul>
  <ul class="abs fcol" style="left:780px"><li>Information</li><li>Buy Reserve</li><li>Shipping Info</li><li>Special Order Info</li><li>Personalization Info</li><li>Gift Coupon</li></ul>
  <ul class="abs fcol" style="left:980px"><li>Our Company</li><li>About Us</li><li>Store Locators</li><li>Privacy &amp; Security</li><li>Terms &amp; Conditions</li></ul>
  <div class="abs follow">Follow Us
    <div class="socials"><span></span><span></span><span></span><span></span><span></span></div>
  </div>
</footer>

<div class="abs partners">
  <span>Our Preferred Partners</span>
  <span class="badge"></span><span class="badge"></span><span class="badge"></span><span class="badge"></span>
  <span style="flex:1"></span>
  <span class="badge"></span><span class="badge"></span><span class="badge"></span><span class="badge"></span><span class="badge"></span><span class="badge"></span>
  <span style="width:38px"></span>
</div>

</body>
</html>
```